Bright Harbor Works Buisness Cards

Provide a business card layout

Paul Wexford
PO Box 742
Alderton ME 04318
paul@thwexample.com

Industry/Entity Type

Business

Font styles to use
Serif

Colors
f04a50

```html
<!DOCTYPE html>
<html lang="en">
<head>
<meta charset="utf-8">
<title>Bright Harbor Works – Business Card</title>
<link href="https://fonts.googleapis.com/css2?family=Cinzel:wght@400&family=Ubuntu:wght@400&display=swap" rel="stylesheet">
<style>
  :root {
    --page-bg: #e8e5e0;
    --card-white: #ffffff;
    --card-dark: #2b2625;
    --accent-red: #f04a50;
    --accent-red-deep: #c93238;
    --name-grey: #4a4a4a;
    --mark-grey: #9a9a9a;
    --contact-white: #f4f2f0;
  }
  html, body {
    margin: 0;
    padding: 0;
    width: 1200px;
    height: 900px;
    overflow: hidden;
    background: var(--page-bg);
  }
  .canvas {
    position: relative;
    width: 1200px;
    height: 900px;
  }
  .business-card {
    position: absolute;
    left: 180px;
    top: 210px;
    width: 840px;
    height: 480px;
    background: var(--card-dark);
    box-shadow: 0 18px 40px rgba(0,0,0,0.25), 0 3px 8px rgba(0,0,0,0.15);
    overflow: hidden;
  }
  .card-shapes {
    position: absolute;
    inset: 0;
    width: 100%;
    height: 100%;
  }
  .brand {
    position: absolute;
    left: 320px;
    top: 58px;
    width: 490px;
    text-align: center;
  }
  .brand-dot {
    display: block;
    width: 54px;
    height: 54px;
    margin: 0 auto 14px 150px;
    border: 2px solid var(--mark-grey);
    border-radius: 50%;
  }
  .brand-name {
    margin: 0;
    font-family: "Cinzel", serif;
    font-weight: 400;
    font-size: 36px;
    letter-spacing: 1px;
    color: var(--name-grey);
    white-space: nowrap;
  }
  .contact {
    position: absolute;
    left: 78px;
    top: 300px;
    font-family: "Ubuntu", sans-serif;
  }
  .contact-name {
    margin: 0 0 12px;
    font-size: 27px;
    font-weight: 400;
    color: var(--accent-red);
  }
  .contact-details {
    margin: 0;
    padding-left: 8px;
    font-style: normal;
    font-size: 25px;
    line-height: 34px;
    color: var(--contact-white);
  }
</style>
</head>
<body>
  <main class="canvas">
    <section class="business-card" aria-label="Bright Harbor Works business card">
      <svg class="card-shapes" viewBox="0 0 840 480" preserveAspectRatio="none" aria-hidden="true">
        <defs>
          <linearGradient id="darkPanel" x1="0" y1="0" x2="0" y2="1">
            <stop offset="0" stop-color="#3a3332"/>
            <stop offset="1" stop-color="#1f1b1a"/>
          </linearGradient>
          <linearGradient id="whitePanel" x1="0" y1="0" x2="0" y2="1">
            <stop offset="0" stop-color="#ffffff"/>
            <stop offset="1" stop-color="#f1f1f1"/>
          </linearGradient>
        </defs>
        <rect class="dark-panel" width="840" height="480" fill="url(#darkPanel)"/>
        <path class="white-panel" d="M0,0 H840 V250 C420,262 150,190 0,2 Z" fill="url(#whitePanel)"/>
        <path class="red-sweep" d="M0,2 C150,190 420,262 840,250" transform="translate(0,6)" fill="none" stroke="var(--accent-red)" stroke-width="8"/>
        <path class="red-sweep-edge" d="M0,2 C150,190 420,262 840,250" transform="translate(0,10)" fill="none" stroke="var(--accent-red-deep)" stroke-width="1.5"/>
      </svg>

      <div class="brand">
        <span class="brand-dot" aria-hidden="true"></span>
        <h1 class="brand-name">Bright Harbor Works</h1>
      </div>

      <div class="contact">
        <h2 class="contact-name">Paul Wexford</h2>
        <address class="contact-details">
          PO Box 742<br>
          Alderton ME 04318<br>
          paul@thwexample.com
        </address>
      </div>
    </section>
  </main>
</body>
</html>
```